Brightwell Giving Inc

We need a full re-design of our non-profit organization website (www.brightwellgiving.org). Ideally, we are looking to make it more attractive, user-friendly, and interactive with our business model.

Please make sure to user colors that ago with our logo.

We need a homepage done and we also need a content page done where we will use for the other pages to fill with content.

Target Market(s)

Clothes/textiles donations.

Industry/Entity Type

Charity

Number of Pages Required

2 page

Colors

Designer to choose colors to be used in the design.

Requirements
Must have
• It must match the styling of our logo and same colors as current website. (www.brightwellgiving.org)
Nice to have
• Sleek homepage that is easy to understand and get our main points across.

```html
<!DOCTYPE html>
<html lang="en">
<head>
<meta charset="utf-8">
<title>Brightwell Giving</title>
<link href="https://fonts.googleapis.com/css2?family=Montserrat:wght@400;500;600;700&display=swap" rel="stylesheet">
<style>
:root{
  --green:#3f7a1c;
  --green-dark:#2f5f14;
  --green-light:#7cbb4a;
  --yellow:#f2c416;
  --yellow-soft:#f4e36a;
  --ink:#3a3a3a;
  --muted:#555;
  --gray-bg:#f4f4f4;
  --footer:#575757;
  --footer-dark:#1e1e1e;
}
*{box-sizing:border-box;margin:0;padding:0}
html,body{width:1200px;height:2862px;overflow:hidden}
body{font-family:'Montserrat',sans-serif;color:var(--ink);background:#fff;position:relative}
.topbar{height:42px;background:var(--green);color:#fff;font-size:12px;font-weight:600;display:flex;justify-content:flex-end;align-items:center;gap:44px;padding-right:82px}
.header{height:103px;position:relative}
.brand{position:absolute;left:99px;top:30px;display:flex;align-items:center;gap:10px}
.brand-mark{width:40px;height:40px;background:var(--yellow)}
.brand-name{font-size:16px;font-weight:700;color:var(--green-dark);line-height:1}
.brand-tag{font-size:9px;color:var(--ink);margin-top:4px}
.nav{position:absolute;right:99px;top:36px;display:flex;align-items:center;gap:26px;font-size:11px;font-weight:600;color:var(--green)}
.nav .active{color:var(--yellow)}
.btn{display:inline-flex;align-items:center;justify-content:center;background:var(--green-dark);color:#fff;border-radius:20px;font-weight:600;font-size:12px;text-transform:uppercase}
.nav .btn{width:104px;height:30px;font-size:11px;margin-left:4px}
.hero{height:488px;position:relative;background:radial-gradient(ellipse at 45% 35%,#8a6a55,#5a4236 45%,#2a211d 90%);color:#fff;text-align:center;padding-top:85px}
.hero h1{font-size:31px;font-weight:500}
.hero h1 span{color:var(--yellow);font-weight:700}
.hero p{width:760px;margin:40px auto 0;font-size:15px;line-height:19px}
.points{position:absolute;left:99px;top:521px;width:1002px;height:242px;background:#fff;box-shadow:0 4px 18px rgba(0,0,0,.12);padding:42px 0 0 258px}
.points li{list-style:none;display:flex;align-items:center;gap:10px;font-size:15px;font-weight:600;color:var(--muted);height:34px;text-transform:uppercase}
.section-title{text-align:center;color:var(--green);font-size:27px;font-weight:700}
.rule{width:136px;height:20px;margin:16px auto 0;border-left:2px solid var(--yellow);border-right:2px solid var(--yellow);position:relative}
.rule::after{content:"";position:absolute;left:0;right:0;top:9px;height:2px;background:var(--yellow)}
.recipients{position:absolute;top:860px;left:0;width:1200px}
.subtitle{text-align:center;font-size:16px;color:var(--muted);margin-top:34px}
.levels{position:absolute;top:207px;left:0;width:1200px}
.level{position:absolute;width:152px;height:162px;background:#fff;box-shadow:0 2px 8px rgba(0,0,0,.12)}
.level .icon{height:102px;display:flex;flex-wrap:wrap;align-content:center;justify-content:center;gap:6px;padding:0 30px}
.level .icon i{width:26px;height:26px;border-radius:50%;background:var(--yellow);border:3px solid var(--green)}
.level .tag{height:60px;background:var(--green-light);color:#fff;text-align:center;font-size:14px;font-weight:700;padding-top:12px;line-height:19px}
.level .tag small{display:block;font-size:14px;font-weight:500}
.more{position:absolute;left:534px;width:132px;height:36px}
.news{position:absolute;top:1414px;left:0;width:1200px;height:662px;background:var(--gray-bg);padding-top:77px}
.card{position:absolute;top:202px;width:267px;height:284px;background:#fff;box-shadow:0 2px 8px rgba(0,0,0,.1)}
.card .photo{height:216px;position:relative}
.card .arrow{position:absolute;right:0;bottom:-26px;width:66px;height:66px;border-radius:50% 0 0 50%;background:#fff;display:flex;align-items:center;justify-content:center}
.card p{padding:18px 70px 0 16px;font-size:12px;line-height:17px;color:var(--muted)}
.finder{position:absolute;top:2076px;left:0;width:1200px;height:166px;background:linear-gradient(90deg,#4e5a66,#8d99a6 40%,#6f7c88 70%,#3e4853);display:flex;align-items:center;padding:0 99px}
.finder h2{color:#fff;font-size:26px;font-weight:700;flex:1}
.zip{width:276px;height:36px;border:2px solid #fff;border-radius:18px;color:#fff;font-size:12px;font-weight:500;padding:10px 20px;margin-right:30px}
.search{width:132px;height:36px;background:#fff;border-radius:18px;color:var(--green-dark);font-size:12px;font-weight:600;display:flex;align-items:center;justify-content:center}
.footer{position:absolute;top:2242px;left:0;width:1200px;height:544px;background:var(--footer)}
.map{position:absolute;left:99px;top:95px;width:649px;height:353px;background:radial-gradient(circle at 30% 30%,#f1e7b0 0,transparent 30%),radial-gradient(circle at 70% 25%,#cfe2b8 0,transparent 30%),radial-gradient(circle at 45% 80%,#f0dc8a 0,transparent 30%),linear-gradient(135deg,#eee9d8,#e1ead2 50%,#ece4cc)}
.badges{position:absolute;left:799px;top:100px;display:flex;gap:14px;align-items:center}
.badges span{width:64px;height:66px;background:var(--yellow-soft);border:2px solid #d9c23a}
.badges span.round{border-radius:50%;width:68px;height:68px;background:var(--yellow)}
.contact{position:absolute;left:802px;top:232px;color:#fff}
.contact h3{font-size:17px;font-weight:700}
.contact .line{width:126px;height:2px;background:var(--yellow);margin:10px 0 26px}
.office{display:flex;gap:42px;height:57px;font-size:11px;line-height:17px}
.office b{font-size:13px;font-weight:700}
.bottom{position:absolute;top:2786px;left:0;width:1200px;height:76px;background:var(--footer-dark);color:#fff;font-size:11px;display:flex;align-items:center;padding-left:448px}
.social{position:absolute;right:98px;top:18px;display:flex;gap:18px}
.social span{width:42px;height:42px;border:2px solid #fff;border-radius:50%}
</style>
</head>
<body>
<div class="topbar"><span>New York: 518-555-0142</span><span>Toll Free: (855) 555-0198</span></div>
<header class="header">
  <div class="brand"><span class="brand-mark"></span><div><div class="brand-name">BRIGHTWELL GIVING</div><div class="brand-tag">Think Globally while Donating Locally</div></div></div>
  <nav class="nav"><span class="active">HOME</span><span>MISSIONS</span><span>HOW IT WORK</span><span>ABOUT US</span><span>SPONSORS</span><span>NEWS</span><span>WALL OF NEEDS</span><span class="btn">Donate</span></nav>
</header>
<section class="hero" role="img" aria-label="Photo of hands joined together in unity">
  <h1>Welcome To <span>Brightwell Giving</span></h1>
  <p>Brightwell Giving is a non-profit organization that was created for one purpose: helping the less fortunate in our country's time of greatest need. Started in 2007, Brightwell Giving has been a dedicated member of its local communities over the past four years. The company's clothing collection efforts have allowed it to provide some of the neediest members of the community to clothe themselves and their families. The company's goal is to ensure that some of the most basic needs of the community's members are met thru the philanthropic efforts of the organizations members and contributors.</p>
</section>
<ul class="points">
  <li><svg width="22" height="18" viewBox="0 0 22 18"><path d="M2 9l6 6L20 2" fill="none" stroke="#f2c416" stroke-width="3"/></svg>We are an open book organization</li>
  <li><svg width="22" height="18" viewBox="0 0 22 18"><path d="M2 9l6 6L20 2" fill="none" stroke="#f2c416" stroke-width="3"/></svg>We are a true 501(c)(3) non-profit organization</li>
  <li><svg width="22" height="18" viewBox="0 0 22 18"><path d="M2 9l6 6L20 2" fill="none" stroke="#f2c416" stroke-width="3"/></svg>Our goal is to be with and within the community</li>
  <li><svg width="22" height="18" viewBox="0 0 22 18"><path d="M2 9l6 6L20 2" fill="none" stroke="#f2c416" stroke-width="3"/></svg>Help disaster victims of Hurricane Irene</li>
  <li><svg width="22" height="18" viewBox="0 0 22 18"><path d="M2 9l6 6L20 2" fill="none" stroke="#f2c416" stroke-width="3"/></svg>Help Hillside Parent &amp; Child Society</li>
</ul>
<section class="recipients">
  <h2 class="section-title">Donation Recipients</h2>
  <div class="rule"></div>
  <p class="subtitle">Think Globally while Donating Locally</p>
  <div class="levels">
    <div class="level" style="left:99px"><div class="icon"><i></i></div><div class="tag">LEVEL 1<small>$1000</small></div></div>
    <div class="level" style="left:311px"><div class="icon"><i></i><i></i></div><div class="tag">LEVEL 2<small>$1000 - $2500</small></div></div>
    <div class="level" style="left:525px"><div class="icon"><i></i><i></i><i></i></div><div class="tag">LEVEL 3<small>$2500 - $5000</small></div></div>
    <div class="level" style="left:738px"><div class="icon"><i></i><i></i><i></i><i></i></div><div class="tag">LEVEL 4<small>$5000 - $10,000</small></div></div>
    <div class="level" style="left:950px"><div class="icon"><i></i><i></i><i></i><i></i><i></i></div><div class="tag">LEVEL 5<small>$10,000 - $25,000</small></div></div>
    <span class="btn more" style="top:230px">Read More</span>
  </div>
</section>
<section class="news">
  <h2 class="section-title">Latest News</h2>
  <div class="rule"></div>
  <article class="card" style="left:99px"><div class="photo" role="img" aria-label="Photo of cupped hands holding string lights" style="background:radial-gradient(circle at 50% 55%,#f3c9a0 0,#e3b08a 18%,transparent 40%),linear-gradient(160deg,#cfe8f6,#7fb8dc)"><span class="arrow"><svg width="30" height="12" viewBox="0 0 30 12"><path d="M0 6h26M21 1l6 5-6 5" fill="none" stroke="#2f5f14" stroke-width="2.5"/></svg></span></div><p>Brightwell Giving created the flyer for inform the people in...</p></article>
  <article class="card" style="left:466px"><div class="photo" role="img" aria-label="Photo of volunteers holding donation boxes" style="background:linear-gradient(180deg,#9fb7cc 0,#6d8fb0 30%,#c9a88c 60%,#d8b98f 80%,#6e8a4e)"><span class="arrow"><svg width="30" height="12" viewBox="0 0 30 12"><path d="M0 6h26M21 1l6 5-6 5" fill="none" stroke="#2f5f14" stroke-width="2.5"/></svg></span></div><p>Brightwell Giving created the flyer for inform the people in...</p></article>
  <article class="card" style="left:832px"><div class="photo" role="img" aria-label="Photo of a family packing donation boxes outdoors" style="background:linear-gradient(160deg,#4a5f33,#7d8a5a 35%,#c2a584 60%,#6f8f4a)"><span class="arrow"><svg width="30" height="12" viewBox="0 0 30 12"><path d="M0 6h26M21 1l6 5-6 5" fill="none" stroke="#2f5f14" stroke-width="2.5"/></svg></span></div><p>Brightwell Giving created the flyer for inform the people in...</p></article>
  <span class="btn more" style="top:551px">See More</span>
</section>
<section class="finder">
  <h2>Find Local Donation Place</h2>
  <div class="zip">ENTER ZIP CODE</div>
  <div class="search">SEARCH</div>
</section>
<footer class="footer">
  <div class="map" role="img" aria-label="Map of donation drop-off locations across upstate New York"></div>
  <div class="badges" role="img" aria-label="Recycling and non-profit certification badges"><span></span><span></span><span></span><span class="round"></span></div>
  <div class="contact">
    <h3>Get in Touch</h3>
    <div class="line"></div>
    <div class="office"><svg width="30" height="34" viewBox="0 0 30 34"><path d="M15 32C7 22 4 17 4 12a11 11 0 0122 0c0 5-3 10-11 20z" fill="none" stroke="#f2c416" stroke-width="2"/><circle cx="15" cy="12" r="4" fill="none" stroke="#f2c416" stroke-width="2"/></svg><div><b>New York Office :</b><br>27 Maple Ridge Rd Athens NY 12015</div></div>
    <div class="office"><svg width="30" height="34" viewBox="0 0 30 34"><path d="M15 32C7 22 4 17 4 12a11 11 0 0122 0c0 5-3 10-11 20z" fill="none" stroke="#f2c416" stroke-width="2"/><circle cx="15" cy="12" r="4" fill="none" stroke="#f2c416" stroke-width="2"/></svg><div><b>Thrift Store :</b><br>118 Linden Ave Hudson NY 12534</div></div>
    <div class="office"><svg width="30" height="34" viewBox="0 0 30 34"><path d="M15 32C7 22 4 17 4 12a11 11 0 0122 0c0 5-3 10-11 20z" fill="none" stroke="#f2c416" stroke-width="2"/><circle cx="15" cy="12" r="4" fill="none" stroke="#f2c416" stroke-width="2"/></svg><div><b>NY Warehouse :</b><br>904 River Rd Catskill NY 12414</div></div>
  </div>
</footer>
<div class="bottom">© 2018 BRIGHTWELL GIVING. ALL RIGHTS RESERVED
  <div class="social" aria-label="Social media links"><span></span><span></span><span></span></div>
</div>
</body>
</html>
```